1/4 page magazine ad

We would like a 1/4 ad in a magazine advertising a doctor in our practice. Dr. Lena Moskit, DC is the only Female Haldrup Certified chiropractor in Ashcombe Falls. We would like the ad to include a large eye catching picture of a woman's pregnant belly, as the Haldrup technique is for pregnant women. Please take a look at our previous ad that we have had done to see some of the elements that we liked in our other ad.

```html
<!DOCTYPE html>
<html lang="en">
<head>
<meta charset="utf-8">
<title>Dr. Lena Moskit, DC – Quarter Page Ad</title>
<link href="https://fonts.googleapis.com/css2?family=Bebas+Neue&display=swap" rel="stylesheet">
<style>
  :root {
    --page-bg: #ececec;
    --ad-black: #0b0b0b;
    --rust: rgba(158, 72, 48, 0.88);
    --skin-hi: #e0805a;
    --skin-mid: #a84a2e;
    --skin-dark: #3a1a10;
    --spine-glow: #ffb27a;
    --brand-red: #7d1414;
    --white: #ffffff;
  }
  * { margin: 0; padding: 0; box-sizing: border-box; }
  html, body {
    width: 1200px; height: 1200px; overflow: hidden;
    background: var(--page-bg);
  }
  .ad {
    position: absolute; left: 201px; top: 84px;
    width: 798px; height: 1032px;
    background: var(--ad-black);
    overflow: hidden;
    font-family: "Bebas Neue", "Oswald", sans-serif;
    color: var(--white);
  }
  .ad__photo {
    position: absolute; left: 330px; top: 0; width: 468px; height: 1032px;
    background:
      radial-gradient(ellipse 22% 45% at 70% 48%, var(--spine-glow) 0%, rgba(255,140,80,0.55) 45%, rgba(0,0,0,0) 100%),
      radial-gradient(ellipse 70% 60% at 55% 50%, var(--skin-hi) 0%, var(--skin-mid) 45%, var(--skin-dark) 80%, var(--ad-black) 100%);
  }
  .ad__wedge {
    position: absolute; inset: 0; width: 798px; height: 1032px;
  }
  .brand {
    position: absolute; left: 72px; top: 41px; width: 403px; height: 99px;
    background: var(--white);
    display: flex; align-items: center; gap: 16px; padding: 0 20px;
  }
  .brand__mark { width: 22px; height: 22px; background: var(--brand-red); flex: none; }
  .brand__name {
    color: var(--brand-red); font-size: 34px; line-height: 1.05; letter-spacing: 0.5px;
  }
  .headline {
    position: absolute; left: 72px; top: 414px;
    font-size: 108px; line-height: 88px; font-weight: 400; letter-spacing: 1px;
  }
  .doctor-bar {
    position: absolute; left: 0; top: 647px; width: 430px; height: 72px;
    background: var(--white);
    display: flex; align-items: center; padding-left: 72px;
  }
  .doctor-bar__name { color: var(--brand-red); font-size: 50px; letter-spacing: 0.5px; padding-top: 4px; }
  .credential {
    position: absolute; left: 72px; top: 775px;
    font-size: 24px; line-height: 30px; letter-spacing: 0.4px;
  }
  .phone {
    position: absolute; left: 70px; top: 890px;
    display: flex; align-items: center; gap: 14px;
    font-size: 52px; letter-spacing: 0.5px;
  }
  .phone__icon { width: 36px; height: 36px; }
</style>
</head>
<body>
  <div class="ad">
    <div class="ad__photo" role="img" aria-label="Photo of a man's bare back holding his neck, with a glowing highlighted spine"></div>

    <svg class="ad__wedge" viewBox="0 0 798 1032" aria-hidden="true">
      <polygon points="798,0 0,435 0,1032 355,1032" fill="var(--rust)"/>
    </svg>

    <div class="brand">
      <span class="brand__mark"></span>
      <span class="brand__name">Harrowgate Spine &amp; Posture Center</span>
    </div>

    <h1 class="headline">Neck or<br>Back Pain?</h1>

    <div class="doctor-bar"><span class="doctor-bar__name">Dr. Lena Moskit, DC</span></div>

    <p class="credential">Female Haldrup Certified<br>Chiropractor in Ashcombe Falls</p>

    <div class="phone">
      <svg class="phone__icon" viewBox="0 0 24 24" aria-hidden="true">
        <path d="M6.6 2.5c.5-.3 1.1-.2 1.5.3l2.2 3c.4.5.3 1.2-.1 1.6l-1.4 1.3c.9 2 2.5 3.7 4.5 4.6l1.3-1.4c.4-.5 1.1-.5 1.6-.1l3 2.2c.5.4.6 1 .3 1.5l-1 1.8c-.6 1-1.8 1.5-2.9 1.2C9.7 17.3 6.7 14.3 5.5 8.3c-.3-1.1.2-2.3 1.2-2.9z" fill="none" stroke="var(--white)" stroke-width="1.8" stroke-linejoin="round"/>
        <path d="M14 3.5a6.5 6.5 0 0 1 6.5 6.5M14 6.8a3.2 3.2 0 0 1 3.2 3.2" fill="none" stroke="var(--white)" stroke-width="1.8" stroke-linecap="round"/>
      </svg>
      <span class="phone__number">555.210.0148</span>
    </div>
  </div>
</body>
</html>
```